Explosive, chemical reaction of creativity!

Web design for a digital marketing company. The unconventional is encouraged!
This is for a cool, young, geographically diverse company (artmingle... you are all part of our team!!!)... we build websites but our real specialty is "search experience optimization".... creating conversion focused content, SEO (including content), and social media.

Target Market(s)

small to medium size businesses, law firms, medical practices, municipalities

Industry/Entity Type

Marketing

Number of Pages Required

2 page

Requirements
Must have
• WOW
• something different and special... we've been playing with a science theme (www.vexmorrow.marketing) but we are open to different looks, layouts, etc.
• we nee a homepage design and an interior page design
• content needs to include: Marketing Catalysts (about us), Our Formula (services), Chemical Reactions(Results/Our Clients),
• FREE Web Prism Audit
• Let us put together an objective snapshot of your digital presence for you.
Nice to have
• we are open to the use of background video (chemical reaction???)
• we are open to cool and different imagery
Should not have
• template look like most other websites

```html
<!DOCTYPE html>
<html lang="en">
<head>
<meta charset="utf-8">
<title>Vexmorrow Digital Marketing</title>
<link href="https://fonts.googleapis.com/css2?family=Raleway:wght@500;600;700;800&family=Open+Sans:wght@400;600&display=swap" rel="stylesheet">
<style>
:root{
  --blue:#1f5ea8;
  --blue-dark:#17497f;
  --navy:#1b2a44;
  --teal:#1fa5a3;
  --orange:#f47a1f;
  --ink:#333a44;
  --muted:#6b717a;
  --band:#e4e6ea;
  --line:#d3d6db;
  --white:#fff;
}
*{box-sizing:border-box;margin:0;padding:0}
html,body{width:1200px;height:3340px;overflow:hidden}
body{font-family:"Open Sans",Arial,sans-serif;color:var(--ink);background:var(--white);position:relative}
.heading{font-family:"Raleway",Arial,sans-serif;font-weight:700;color:var(--ink);text-transform:uppercase;text-align:center;font-size:27px;letter-spacing:.5px;position:absolute;left:0;width:1200px}
.subheading{font-family:"Raleway",Arial,sans-serif;font-size:17px;color:var(--ink);text-align:center;position:absolute;left:0;width:1200px}
.btn{position:absolute;background:linear-gradient(#2f72bf,var(--blue-dark));color:#fff;font-family:"Raleway",Arial,sans-serif;font-weight:700;font-size:12px;text-transform:uppercase;display:flex;align-items:center;justify-content:center;letter-spacing:.4px}

/* header */
.site-header{position:absolute;top:0;left:0;width:1200px;height:82px;background:#fff}
.brand{position:absolute;left:56px;top:24px;display:flex;align-items:center;gap:10px}
.brand-mark{width:32px;height:32px;background:var(--blue)}
.brand-name{font-family:"Raleway",Arial,sans-serif;font-weight:800;font-size:16px;color:var(--blue);text-transform:uppercase;letter-spacing:.6px;line-height:1}
.main-nav{position:absolute;right:56px;top:35px;display:flex;gap:48px;font-family:"Raleway",Arial,sans-serif;font-weight:600;font-size:12px;text-transform:uppercase;color:var(--navy)}

/* hero */
.hero{position:absolute;top:82px;left:0;width:1200px;height:570px}
.hero-photo{position:absolute;inset:0;background:linear-gradient(90deg,#6f7478 0%,#7d8389 35%,#3e4f72 65%,#1e2c4a 100%)}
.hero-copy{position:absolute;left:100px;top:160px;color:#fff;font-family:"Raleway",Arial,sans-serif}
.hero-kicker{font-weight:700;font-size:21px;text-transform:uppercase;letter-spacing:.5px}
.hero-title{font-weight:700;font-size:21px;text-transform:uppercase;line-height:32px;margin-top:18px;letter-spacing:.3px}
.hero-text{font-size:17px;line-height:28px;margin-top:14px;font-weight:500}
.hero .btn{left:100px;top:381px;width:167px;height:45px}
.hero-dots{position:absolute;left:580px;top:544px;display:flex;gap:6px}
.hero-dots span{width:7px;height:7px;border-radius:50%;background:rgba(255,255,255,.5)}
.hero-dots span:first-child{background:#fff}

/* intro */
.intro-text{position:absolute;left:200px;width:800px;top:810px;text-align:center;font-size:12px;line-height:22px;color:var(--muted)}

/* stats */
.stat{position:absolute;display:flex;align-items:center;gap:16px}
.stat-badge{width:78px;height:78px;border-radius:50%;color:#fff;font-family:"Raleway",Arial,sans-serif;font-weight:700;font-size:27px;display:flex;align-items:center;justify-content:center;flex:none}
.stat-badge.teal{background:var(--teal)}
.stat-badge.orange{background:var(--orange)}
.stat-label{font-size:12px;line-height:20px;color:var(--muted);width:150px}

/* formula */
.device{position:absolute;left:211px;top:1425px;width:248px;height:456px;border-radius:36px;background:linear-gradient(#f4f5f7,#dcdfe4);border:2px solid #c8ccd2}
.device-screen{position:absolute;left:20px;top:62px;width:204px;height:322px;background:#fff;border:3px solid #222}
.device-name{position:absolute;top:150px;width:100%;text-align:center;font-family:"Raleway",Arial,sans-serif;font-weight:800;font-size:15px;color:var(--navy);text-transform:uppercase}
.device-button{position:absolute;left:104px;top:398px;width:38px;height:38px;border-radius:50%;border:2px solid #c8ccd2}
.feature{position:absolute;left:590px;display:flex;gap:27px}
.feature-icon{width:73px;height:73px;border-radius:50%;background:var(--blue);flex:none;display:flex;align-items:center;justify-content:center}
.feature h3{font-family:"Raleway",Arial,sans-serif;font-weight:600;font-size:14px;color:var(--ink);margin-top:2px}
.feature p{font-size:12px;line-height:22px;color:var(--muted);width:290px;margin-top:8px}

/* posts */
.post{position:absolute;top:2373px;width:229px}
.post-image{height:203px}
.post h3{font-family:"Raleway",Arial,sans-serif;font-weight:600;font-size:14px;line-height:24px;color:var(--ink);margin-top:24px}
.post p{font-size:11px;line-height:22px;color:var(--muted);margin-top:10px}

/* contact */
.contact{position:absolute;top:2856px;left:0;width:1200px;height:427px;background:var(--band)}
.contact-item{position:absolute;left:100px;display:flex;align-items:center;gap:18px;font-size:11px;line-height:18px;color:var(--muted)}
.contact-icon{width:38px;height:38px;border-radius:50%;display:flex;align-items:center;justify-content:center;flex:none}
.field{position:absolute;background:#fff;border:1px solid var(--line);font-size:11px;color:var(--muted);padding:10px 14px}

/* footer */
.site-footer{position:absolute;top:3283px;left:0;width:1200px;height:57px;background:var(--blue);color:#fff;font-size:11px}
.copyright{position:absolute;left:100px;top:21px}
.social{position:absolute;right:100px;top:13px;display:flex;align-items:center;gap:8px}
.social span.dot{width:28px;height:28px;border-radius:50%;background:#fff}
</style>
</head>
<body>

<header class="site-header">
  <div class="brand"><span class="brand-mark"></span><span class="brand-name">Vexmorrow Digital Marketing</span></div>
  <nav class="main-nav"><span>Home</span><span>Marketing Catalysts</span><span>Our Formula</span><span>Chemical Reactions</span><span>Contact Us</span></nav>
</header>

<section class="hero">
  <div class="hero-photo" role="img" aria-label="Photo of a man in a blue shirt and tie holding a glass globe"></div>
  <div class="hero-copy">
    <div class="hero-kicker">Free Web Prism Audit</div>
    <div class="hero-title">Let us put together an objective snapshot<br>of your digital presence for you.</div>
    <div class="hero-text">Sales is the chemical reaction that results from<br>"our formula" which is the right combination of our digital<br>marketing services.</div>
  </div>
  <div class="btn">Read more info</div>
  <div class="hero-dots"><span></span><span></span><span></span><span></span></div>
</section>

<section class="intro">
  <h2 class="heading" style="top:724px">Using data for success</h2>
  <p class="subheading" style="top:768px">Search Engine Optimization has been replaced with Search Experience Optimization.</p>
  <p class="intro-text">SALES is the end result of everything we do. It is why companies exists. It's why we market. It's why your business is online. Our job is to help you maximize your opportunity online to build your brand, get found by new customers and, ultimately, generate SALES!</p>
  <div class="btn" style="left:519px;top:879px;width:162px;height:43px">Read more info</div>
</section>

<section class="catalyst-facts">
  <h2 class="heading" style="top:1005px">Some facts about our catalysts</h2>
  <p class="subheading" style="top:1049px">Working together to create change.</p>
  <div class="stat" style="left:100px;top:1123px"><div class="stat-badge teal">93%</div><div class="stat-label" style="width:150px">Online experiences begin with a search engine</div></div>
  <div class="stat" style="left:365px;top:1123px"><div class="stat-badge teal">70%</div><div class="stat-label" style="width:150px">Of the links search users click on are organic</div></div>
  <div class="stat" style="left:639px;top:1123px"><div class="stat-badge teal">70%</div><div class="stat-label" style="width:125px">Of US population has at least one social networking profile</div></div>
  <div class="stat" style="left:890px;top:1123px"><div class="stat-badge teal">50%</div><div class="stat-label" style="width:135px">Of companies are using digital marketing but don't have a plan</div></div>
</section>

<section class="formula">
  <h2 class="heading" style="top:1305px">The perfect digital marketing formula!</h2>
  <p class="subheading" style="top:1347px">Get the right message in front of the right people.</p>
  <div class="device">
    <div class="device-screen" role="img" aria-label="Phone screen showing molecule illustrations around the company name">
      <div class="device-name">Vexmorrow<br>Digital Marketing</div>
    </div>
    <div class="device-button"></div>
  </div>
  <div class="feature" style="top:1474px">
    <div class="feature-icon"><svg width="32" height="28" viewBox="0 0 32 28" fill="none" stroke="#fff" stroke-width="2"><rect x="2" y="2" width="28" height="18"/><path d="M12 26h8M16 20v6"/></svg></div>
    <div><h3>Website</h3><p>You've got 10 seconds to grab the attention of a site viewer. We build for appearance, content, and functionality: it's a conversion causal nexus!</p></div>
  </div>
  <div class="feature" style="top:1612px">
    <div class="feature-icon"><svg width="32" height="28" viewBox="0 0 32 28" fill="none" stroke="#fff" stroke-width="2"><path d="M2 4h18v12H9l-5 4v-4H2z"/><path d="M24 9h6v12h-2v4l-5-4H14v-3"/></svg></div>
    <div><h3>Content</h3><p>Content is the most powerful element of our formula... it creates need, provokes emotion and sparks action.</p></div>
  </div>
  <div class="feature" style="top:1752px">
    <div class="feature-icon"><svg width="30" height="28" viewBox="0 0 30 28" fill="none" stroke="#fff" stroke-width="2"><path d="M2 2h26v18H10l-6 5v-5H2z"/><path d="M8 8h14M8 13h10"/></svg></div>
    <div><h3>Social</h3><p>We are obsessed with the latest trends and are always testing new ways to cultivate both following and engagement.</p></div>
  </div>
</section>

<section class="team-facts">
  <h2 class="heading" style="top:1982px">Some facts about our catalysts</h2>
  <p class="subheading" style="top:2024px">Working together to create change.</p>
  <div class="stat" style="left:100px;top:2098px"><div class="stat-badge orange">35</div><div class="stat-label">Years Combined Marketing Experience</div></div>
  <div class="stat" style="left:400px;top:2098px"><div class="stat-badge orange">10</div><div class="stat-label">Years Search Engine Optimization Experience</div></div>
  <div class="stat" style="left:682px;top:2098px"><div class="stat-badge orange">234</div><div class="stat-label" style="width:120px">Websites created</div></div>
  <div class="stat" style="left:925px;top:2098px"><div class="stat-badge orange">1</div><div class="stat-label" style="width:100px">Amazing team</div></div>
</section>

<section class="posts">
  <h2 class="heading" style="top:2265px">Recent posts</h2>
  <p class="subheading" style="top:2306px">We also play Quest Arena, Galaxy Saga fans, and love burgers and beer.</p>
  <article class="post" style="left:100px">
    <div class="post-image" role="img" aria-label="Photo of blue signs with social sharing words" style="background:linear-gradient(#4a8fd6,#2a66b0)"></div>
    <h3>A Little Bird Told Me<br>– 5 Reasons for Tweeting</h3>
    <p>There's a thin red line between social media use and networking. Sometimes the two merge into a perfect harmony of conversation and resolution. Other times (perhaps too often), it's just cat pictures and quirky quotes.</p>
  </article>
  <article class="post" style="left:358px">
    <div class="post-image" role="img" aria-label="Photo of a person among glowing digital light streaks" style="background:linear-gradient(#27303c,#0f141c)"></div>
    <h3>The Revolution Will Now<br>Be Optimized</h3>
    <p>There's a thin red line between social media use and networking. Sometimes the two merge into a perfect harmony of conversation and resolution. Other times (perhaps too often), it's just cat pictures and quirky quotes.</p>
  </article>
  <article class="post" style="left:616px">
    <div class="post-image" role="img" aria-label="Photo of a person wearing smart glasses" style="background:linear-gradient(#d9d6d2,#a99a8e)"></div>
    <h3>Search Giant's Fast-Loading Tech<br>Encourages</h3>
    <p>There's a thin red line between social media use and networking. Sometimes the two merge into a perfect harmony of conversation and resolution. Other times (perhaps too often), it's just cat pictures and quirky quotes.</p>
  </article>
  <article class="post" style="left:873px">
    <div class="post-image" role="img" aria-label="Illustration of a glowing blue digital head profile" style="background:linear-gradient(135deg,#0c2a4a,#1f6fb3)"></div>
    <h3>Take Your Business to the Next<br>Level: Spring Summit Edition</h3>
    <p>There's a thin red line between social media use and networking. Sometimes the two merge into a perfect harmony of conversation and resolution. Other times (perhaps too often), it's just cat pictures and quirky quotes.</p>
  </article>
</section>

<section class="contact">
  <h2 class="heading" style="top:62px">Contact us</h2>
  <p class="subheading" style="top:105px">We can't wait to hear from you!</p>
  <div class="contact-item" style="top:186px"><span class="contact-icon" style="background:var(--blue)"><svg width="14" height="18" viewBox="0 0 14 18"><path d="M7 0a7 7 0 0 0-7 7c0 5 7 11 7 11s7-6 7-11a7 7 0 0 0-7-7z" fill="#fff"/><circle cx="7" cy="7" r="2.5" fill="#1f5ea8"/></svg></span><span>2870 Orchard Row, Suite 410<br>Fairhaven, TX 75990</span></div>
  <div class="contact-item" style="top:255px"><span class="contact-icon" style="background:var(--teal)"><svg width="16" height="16" viewBox="0 0 16 16"><path d="M3 1l3 3-2 2c1 2 3 4 5 5l2-2 3 3-2 3C7 15 1 9 1 3z" fill="#fff"/></svg></span><span>800-555-0142</span></div>
  <div class="contact-item" style="top:324px"><span class="contact-icon" style="background:var(--orange)"><svg width="18" height="16" viewBox="0 0 18 16" fill="none" stroke="#fff" stroke-width="2"><path d="M2 10V8a7 7 0 0 1 14 0v2"/><rect x="1" y="9" width="4" height="6" fill="#fff"/><rect x="13" y="9" width="4" height="6" fill="#fff"/></svg></span><span>Live Support</span></div>
  <div class="field" style="left:434px;top:183px;width:318px;height:40px">Name</div>
  <div class="field" style="left:434px;top:242px;width:318px;height:41px">Email</div>
  <div class="field" style="left:434px;top:303px;width:318px;height:40px">Phone</div>
  <div class="field" style="left:777px;top:183px;width:316px;height:100px">Message</div>
  <div class="btn" style="left:777px;top:303px;width:316px;height:38px">Send message</div>
</section>

<footer class="site-footer">
  <span class="copyright">Copyrights, 2016. Vexmorrow digital marketing. All rights reserved.</span>
  <div class="social"><span style="margin-right:4px">Follow Us :</span><span class="dot"></span><span class="dot"></span><span class="dot"></span></div>
</footer>

</body>
</html>
```